Design for web based travel expence program

We need a design template for a web based travel expence program we have created. The current design is based on a standard framework, and it needs to be "spiced" up.
Please notice that there are only 3-4 screen shots that needs an "upspice" of the design. No complete web design is expected for this price. For the right designer we have many more jobs coming up!
Velquor Accounting is a Scandinavian accounting company with offices in Norway (Oslo) and Stockholm (Sweden). Our goal is to be a proactive accounting company known for trouble-free solutions and wide knowledge about what we do. We have created an "easy" accounting program enabling clients to take picture of vouchers, upload them to our portal and gather them to a travel expense scheme that can be approved and sent directly into an accounting program.
The program is pure web based and created with sophisticated programming code, but only with a standard framework as design template. We need a touch of professional design that easily can be implemented “on top” of the framework.
We are thinking that the designer should add icons and create the squared elements a bit rounder and with a more beautiful touch.
We are looking for a designer that preferably can create CSS files with an improved design, though the first step should be to create some pictures/Photshop examples on how it could look like. The files we have uploaded are the screen shots that needs to be improved with a better design.
Target Market(s)
All type of businesses, but the end user is in focus. The program is designed to be easy-to-learn and very useful for all persons dealing with travel expence forms.
Industry/Entity Type
Accounting

```html
<!DOCTYPE html>
<html lang="no">
<head>
<meta charset="utf-8">
<title>Reiseregning – skjermoppsett</title>
<link href="https://fonts.googleapis.com/css2?family=Arimo:wght@400;700&display=swap" rel="stylesheet">
<style>
:root{
  --sidebar:#1c1f26;
  --sidebar-active:#3b3e45;
  --sidebar-text:#d6d8dc;
  --rail:#87c9e6;
  --blue:#1b64b0;
  --blue-dark:#0f4f95;
  --blue-text:#1e6cb8;
  --badge:#2aa3dc;
  --label-blue:#86c8e6;
  --grey-btn-top:#7b7b79;
  --grey-btn-bot:#4a4a48;
  --light-btn-top:#f7f7f7;
  --light-btn-bot:#d3d3d3;
  --line:#e4e4e4;
  --panel:#f4f4f4;
  --table-head:#ebebeb;
  --text:#555;
  --muted:#999;
  --step:#8a8a8a;
}
*{box-sizing:border-box;margin:0;padding:0}
html,body{width:1200px;height:1000px;overflow:hidden;background:#fff}
body{position:relative;font-family:"Arimo",Arial,sans-serif;color:var(--text);font-size:9px}
.abs{position:absolute}

.sidebar{left:0;width:158px;background:var(--sidebar)}
.rail{left:158px;width:165px;background:var(--rail)}
.nav-item{position:absolute;left:0;width:158px;height:30px;line-height:30px;padding-left:36px;font-size:11px;color:var(--sidebar-text)}
.nav-item.is-active{background:var(--sidebar-active)}
.badge{position:absolute;left:112px;top:7px;width:16px;height:16px;border-radius:50%;background:var(--badge);color:#fff;font-size:8px;font-weight:700;line-height:16px;text-align:center;padding:0}

.rail-btn{position:absolute;left:170px;width:141px;height:31px;border-radius:3px;font-size:8px;line-height:31px;text-align:center;color:#fff;background:linear-gradient(var(--grey-btn-top),var(--grey-btn-bot))}
.rail-btn.is-light{color:#444;background:linear-gradient(var(--light-btn-top),var(--light-btn-bot))}
.rail-btn.is-blue{background:linear-gradient(#2a79c4,var(--blue-dark))}

.filter-card{left:170px;top:51px;width:141px;height:120px;background:#fff;border-radius:4px;overflow:hidden}
.filter-card__head{height:28px;line-height:28px;text-align:center;background:linear-gradient(#2a79c4,var(--blue-dark));color:#fff;font-weight:700;font-size:8px}
.filter-card ul{list-style:none;margin:14px 23px 0 17px}
.filter-card li{font-size:8px;color:#666;padding:4px 0 3px;border-bottom:1px solid #d8d8d8}
.filter-card li:last-child{border:0}

.field{position:absolute;border:1px solid #dcdcdc;background:#fff;font-size:8px;color:#999;padding-left:12px}
.hline{position:absolute;height:1px;background:var(--line)}
.cell{position:absolute;font-size:8px;color:#777}
.cell.head{font-size:11px;color:var(--blue-text)}
.step{position:absolute;font-size:58px;color:var(--step);font-weight:400}

.title{position:absolute;left:371px;font-size:14px;color:var(--blue-text);letter-spacing:.3px}
.status{position:absolute;left:870px;font-size:10px;color:var(--muted)}
.tab{position:absolute;top:0;height:32px;width:88px;line-height:32px;text-align:center;font-size:8px;border:1px solid #dcdcdc;background:#eee;color:#555}
.tab.is-active{background:#fff;color:var(--blue-text);border-bottom-color:#fff;z-index:1}
.tabs{position:absolute;left:373px;width:176px;height:32px}
.panel-box{position:absolute;left:373px;width:416px;border:1px solid #dcdcdc;background:#fff}

.btn{position:absolute;background:linear-gradient(#2a79c4,var(--blue-dark));color:#fff;font-weight:700;font-size:8px;text-align:center;border-radius:2px}

.grey-box{position:absolute;background:var(--panel)}
.box-title{position:absolute;font-size:10px;color:var(--blue-text)}
.small{position:absolute;font-size:7.5px;color:#777}

.receipt{position:absolute;width:114px;height:79px;background:#fff}
.receipt__tag{position:absolute;left:2px;top:2px;width:110px;height:19px;background:var(--label-blue);color:#fff;font-size:8.5px;line-height:19px;padding-left:11px}
.receipt__date{position:absolute;left:13px;top:28px;font-size:7.5px;color:#555;display:flex;align-items:center;gap:6px}
.receipt__amount{position:absolute;left:13px;top:43px;font-size:10px;color:#444}
.receipt__note{position:absolute;left:13px;top:60px;font-size:6.5px;color:#777}
</style>
</head>
<body>

<!-- Screen 1: overview -->
<div class="abs sidebar" style="top:0;height:184px">
  <div class="nav-item is-active" style="top:15px">Refusjoner</div>
  <div class="nav-item" style="top:48px">Kvitteringer<span class="badge">2</span></div>
</div>
<div class="abs rail" style="top:0;height:184px"></div>
<div class="rail-btn" style="top:14px">Lorem ipsum dolor sit</div>
<div class="abs filter-card">
  <div class="filter-card__head">Lorem ipsum dolor sit</div>
  <ul><li>All sent (2)</li><li>Sendt (0)</li><li>Refundert (0)</li></ul>
</div>

<div class="field" style="left:373px;top:13px;width:182px;height:27px"></div>
<div class="hline" style="left:373px;top:46px;width:630px"></div>
<div class="cell head" style="left:373px;top:52px">Heading</div>
<div class="cell head" style="left:533px;top:52px">Heading</div>
<div class="cell head" style="left:693px;top:52px">Heading</div>
<div class="cell head" style="left:853px;top:52px">Heading</div>
<div class="hline" style="left:373px;top:68px;width:630px"></div>
<div class="cell" style="left:373px;top:75px">Lorem Ipsum</div>
<div class="cell" style="left:533px;top:75px">Lorem Ipsum</div>
<div class="cell" style="left:693px;top:75px">Lorem Ipsum</div>
<div class="cell" style="left:853px;top:75px">Lorem Ipsum</div>
<div class="hline" style="left:373px;top:91px;width:630px"></div>
<div class="cell" style="left:373px;top:98px">Lorem Ipsum</div>
<div class="cell" style="left:533px;top:98px">Lorem Ipsum</div>
<div class="cell" style="left:693px;top:98px">Lorem Ipsum</div>
<div class="cell" style="left:853px;top:98px">Lorem Ipsum</div>
<div class="step" style="left:1093px;top:50px">1</div>

<!-- Screen 2: refund detail -->
<div class="abs sidebar" style="top:186px;height:366px">
  <div class="nav-item is-active" style="top:2px">Refusjoner</div>
  <div class="nav-item" style="top:35px">Kvitteringer<span class="badge">2</span></div>
</div>
<div class="abs rail" style="top:186px;height:366px"></div>
<div class="rail-btn" style="top:187px">Lorem ipsum dolor sit</div>
<div class="rail-btn is-light" style="top:222px">Lorem ipsum dolor sit</div>
<div class="rail-btn is-blue" style="top:258px">Lorem ipsum dolor sit</div>
<div class="rail-btn" style="top:293px">Lorem ipsum dolor sit</div>

<div class="title" style="top:194px">REISE UKRAINA</div>
<div class="status" style="top:203px">Status: Lorem Ipsum</div>
<div class="hline" style="left:371px;top:219px;width:777px"></div>

<div class="tabs" style="top:246px">
  <div class="tab is-active" style="left:0">Lag refusion</div>
  <div class="tab" style="left:88px">Send</div>
</div>
<div class="panel-box" style="top:277px;height:240px">
  <div class="cell" style="left:19px;top:27px;font-size:9px;color:#555">Reise Ukraina</div>
  <div class="abs" style="left:19px;top:49px;width:376px;height:26px;background:var(--table-head)"></div>
  <div class="cell" style="left:53px;top:57px;color:var(--blue-dark);font-weight:700">Heading</div>
  <div class="cell" style="left:176px;top:57px;color:var(--blue-dark);font-weight:700">Heading</div>
  <div class="cell" style="left:290px;top:57px;color:var(--blue-dark);font-weight:700">Heading</div>
  <div class="hline" style="left:19px;top:76px;width:376px"></div>
  <div class="cell" style="left:53px;top:84px">Lorem Ipsum</div>
  <div class="cell" style="left:176px;top:84px">12-12-2014</div>
  <div class="cell" style="left:290px;top:84px">1853.00</div>
  <div class="hline" style="left:19px;top:99px;width:376px"></div>
  <div class="cell" style="left:53px;top:108px">Lorem Ipsum</div>
  <div class="cell" style="left:176px;top:108px">12-12-2014</div>
  <div class="cell" style="left:290px;top:108px">1853.00</div>
  <div class="hline" style="left:19px;top:125px;width:376px"></div>
  <div class="cell" style="left:53px;top:136px">Lorem Ipsum</div>
  <div class="cell" style="left:176px;top:136px">12-12-2014</div>
  <div class="cell" style="left:290px;top:136px">1853.00</div>
  <div class="abs" style="left:19px;top:152px;width:376px;height:24px;background:var(--table-head)"></div>
  <div class="cell" style="left:53px;top:160px;color:#666">TOTAL</div>
  <div class="cell" style="left:290px;top:160px;color:#444;font-weight:700">1853.00</div>
</div>

<div class="field" style="left:869px;top:245px;width:182px;height:29px;line-height:27px">Mottaker</div>
<div class="btn" style="left:1061px;top:245px;width:85px;height:29px;line-height:29px">SEND&nbsp; REFUSJON</div>
<div class="step" style="left:1091px;top:342px">2</div>

<!-- Screen 3: new expense -->
<div class="abs sidebar" style="top:554px;height:446px">
  <div class="nav-item is-active" style="top:15px">Refusjoner</div>
  <div class="nav-item" style="top:49px">Kvitteringer<span class="badge">2</span></div>
</div>
<div class="abs rail" style="top:554px;height:446px"></div>
<div class="rail-btn" style="top:569px">Lorem ipsum dolor sit</div>
<div class="rail-btn is-light" style="top:604px">Lorem ipsum dolor sit</div>
<div class="rail-btn is-blue" style="top:640px">Lorem ipsum dolor sit</div>
<div class="rail-btn" style="top:675px">Lorem ipsum dolor sit</div>

<div class="title" style="top:575px">UTLEGG JUNI</div>
<div class="status" style="top:584px">Status: Lorem Ipsum</div>
<div class="hline" style="left:371px;top:600px;width:777px"></div>

<div class="tabs" style="top:628px">
  <div class="tab is-active" style="left:0">Lag refusion</div>
  <div class="tab" style="left:88px">Send</div>
</div>
<div class="panel-box" style="top:659px;height:69px">
  <div class="cell" style="left:20px;top:28px;font-size:9px;color:#444">Tittel</div>
  <div class="field" style="left:86px;top:20px;width:209px;height:24px;line-height:22px;color:#666">Utlegg Juni</div>
</div>

<div class="grey-box" style="left:373px;top:753px;width:192px;height:145px">
  <div class="box-title" style="left:20px;top:19px">Lorem Ipsum</div>
  <div class="hline" style="left:20px;top:41px;width:150px;background:#ddd"></div>
  <div class="small" style="left:21px;top:52px">Antall: 3</div>
  <div class="small" style="left:21px;top:69px">Antall: 3</div>
  <div class="hline" style="left:20px;top:95px;width:150px;background:#ddd"></div>
  <div class="btn" style="left:20px;top:107px;width:69px;height:23px;line-height:23px">Lorem Ipsum</div>
</div>

<div class="grey-box" style="left:581px;top:753px;width:208px;height:243px">
  <div class="box-title" style="left:20px;top:19px">Lorem Ipsum</div>
  <div class="hline" style="left:20px;top:41px;width:173px;background:#ddd"></div>
  <div class="small" style="left:22px;top:60px">Formal</div>
  <div class="field" style="left:77px;top:55px;width:116px;height:21px"></div>
  <div class="small" style="left:22px;top:87px">Destinasjon</div>
  <div class="field" style="left:77px;top:82px;width:116px;height:21px"></div>
  <div class="small" style="left:22px;top:115px">Fra</div>
  <div class="field" style="left:77px;top:109px;width:116px;height:21px"></div>
  <div class="small" style="left:22px;top:143px">Til</div>
  <div class="field" style="left:77px;top:136px;width:116px;height:21px"></div>
  <div class="hline" style="left:20px;top:184px;width:173px;background:#ddd"></div>
  <div class="small" style="left:20px;top:197px;color:var(--blue-text)">Lorem Ipsum</div>
  <div class="small" style="left:20px;top:210px">Antall: 3</div>
  <div class="btn" style="left:77px;top:192px;width:51px;height:19px;line-height:19px">Lorem</div>
  <div class="btn" style="left:133px;top:192px;width:60px;height:19px;line-height:19px">Lorem Ipsum</div>
</div>

<div class="grey-box" style="left:870px;top:628px;width:276px;height:255px">
  <div class="abs" style="left:14px;top:12px;font-size:10px;color:#555">Ledige Kvitteringer</div>
  <div class="hline" style="left:14px;top:30px;width:248px;background:#ddd"></div>

  <div class="receipt" style="left:14px;top:49px">
    <div class="receipt__tag">Elektronikk</div>
    <div class="receipt__date"><svg width="9" height="9" viewBox="0 0 9 9" aria-hidden="true"><rect x="0.5" y="1.5" width="8" height="7" fill="none" stroke="#555"/><rect x="0.5" y="1.5" width="8" height="2" fill="#555"/><rect x="2" y="5" width="1.5" height="1.5" fill="#555"/><rect x="5" y="5" width="1.5" height="1.5" fill="#555"/></svg>12-12-2014</div>
    <div class="receipt__amount">$ 100</div>
    <div class="receipt__note">Comment : 1</div>
  </div>
  <div class="receipt" style="left:147px;top:49px">
    <div class="receipt__tag">Elektronikk</div>
    <div class="receipt__date"><svg width="9" height="9" viewBox="0 0 9 9" aria-hidden="true"><rect x="0.5" y="1.5" width="8" height="7" fill="none" stroke="#555"/><rect x="0.5" y="1.5" width="8" height="2" fill="#555"/><rect x="2" y="5" width="1.5" height="1.5" fill="#555"/><rect x="5" y="5" width="1.5" height="1.5" fill="#555"/></svg>12-12-2014</div>
    <div class="receipt__amount">$ 100</div>
    <div class="receipt__note">Comment : 1</div>
  </div>
  <div class="receipt" style="left:14px;top:146px">
    <div class="receipt__tag">Elektronikk</div>
    <div class="receipt__date"><svg width="9" height="9" viewBox="0 0 9 9" aria-hidden="true"><rect x="0.5" y="1.5" width="8" height="7" fill="none" stroke="#555"/><rect x="0.5" y="1.5" width="8" height="2" fill="#555"/><rect x="2" y="5" width="1.5" height="1.5" fill="#555"/><rect x="5" y="5" width="1.5" height="1.5" fill="#555"/></svg>12-12-2014</div>
    <div class="receipt__amount">$ 100</div>
    <div class="receipt__note">Comment : 1</div>
  </div>
</div>
<div class="step" style="left:1091px;top:893px">3</div>

</body>
</html>
```